Harwick Assurance Partners Ltd needs a business card and logo

We need a logo for documents, invoices etc and a business card to match. We are a health auditing, training and consulting company based in NZ and working in both Australia and NZ. We ensure health organisations meet all their compliance requirements and develop expertise in the health auditing sector. The design should in some way reflect either symbols for quality management in the health sector.

Target Market(s)

Health providers and those wishing to increase their capability in meeting and understanding compliance requirements

Industry/Entity Type

Business

Contact Information for Business Card

Logo plus contact details

Logo Text

Health auditing, consultancy and training

Requirements
Must have
• Name and contact details director: Molly Strand, mstrand@hap-example.co.nz, PO Box 318, Warkworth, NZ, cell +6427391065

```html
<!DOCTYPE html>
<html lang="en">
<head>
<meta charset="utf-8">
<title>Harwick Assurance Partners Ltd – Business Card</title>
<link rel="stylesheet" href="https://fonts.googleapis.com/css2?family=Lato:wght@400;700&family=Poppins:wght@400&display=swap">
<style>
  :root {
    --backdrop: #d5dde0;
    --card-light: #ffffff;
    --card-dark: #1e1e1e;
    --brand-blue: #1a6fb8;
    --brand-red: #e0201c;
    --ink: #111111;
  }
  * { margin: 0; padding: 0; box-sizing: border-box; }
  html, body {
    width: 1181px;
    height: 1200px;
    overflow: hidden;
    background: var(--backdrop);
  }
  .canvas { position: relative; width: 1181px; height: 1200px; }

  .card {
    position: absolute;
    left: 247px;
    width: 669px;
    border-radius: 22px;
  }
  .card--front { top: 90px; height: 410px; background: var(--card-light); }
  .card--back  { top: 665px; height: 395px; background: var(--card-dark); }

  .identity {
    position: absolute;
    left: 22px;
    top: 30px;
    height: 63px;
    padding-left: 16px;
    border-left: 6px solid var(--brand-blue);
    font-family: "Poppins", sans-serif;
  }
  .identity__name { font-size: 28px; line-height: 1.1; color: var(--ink); padding-top: 3px; }
  .identity__role { font-size: 17px; line-height: 1.2; color: var(--brand-blue); }

  .contacts {
    position: absolute;
    left: 22px;
    top: 293px;
    list-style: none;
    font-family: "Lato", sans-serif;
    font-size: 17px;
    color: var(--ink);
  }
  .contacts__item {
    display: flex;
    align-items: center;
    height: 30.5px;
  }
  .contacts__icon { width: 16px; height: 16px; margin-right: 10px; flex: none; }

  .wordmark {
    position: absolute;
    display: flex;
    align-items: center;
    font-family: "Lato", sans-serif;
    font-weight: 700;
    color: var(--brand-blue);
  }
  .wordmark__ring {
    flex: none;
    border-radius: 50%;
    border-style: solid;
    border-color: var(--brand-blue);
  }
  .wordmark__text { line-height: 1.05; }

  .card--front .wordmark { right: 30px; top: 292px; }
  .card--front .wordmark__ring { width: 54px; height: 54px; border-width: 7px; margin-right: 14px; }
  .card--front .wordmark__text { font-size: 25px; }

  .card--back .wordmark { left: 123px; top: 140px; }
  .card--back .wordmark__ring { width: 82px; height: 82px; border-width: 10px; margin-right: 22px; }
  .card--back .wordmark__text { font-size: 38px; }
</style>
</head>
<body>
<main class="canvas">

  <section class="card card--front" aria-label="Business card front">
    <div class="identity">
      <p class="identity__name">Molly Strand</p>
      <p class="identity__role">Director</p>
    </div>

    <ul class="contacts">
      <li class="contacts__item">
        <svg class="contacts__icon" viewBox="0 0 16 16" aria-hidden="true">
          <rect x="1" y="5" width="14" height="9" fill="var(--brand-red)"/>
          <path d="M1 5 L8 10 L15 5" fill="none" stroke="#fff" stroke-width="1.2"/>
        </svg>
        mstrand@hap-example.co.nz
      </li>
      <li class="contacts__item">
        <svg class="contacts__icon" viewBox="0 0 16 16" aria-hidden="true">
          <rect x="4" y="1" width="8" height="14" rx="1.5" fill="none" stroke="var(--brand-red)" stroke-width="1.6"/>
          <circle cx="8" cy="12.5" r="0.9" fill="var(--brand-red)"/>
        </svg>
        +6427391065
      </li>
      <li class="contacts__item">
        <svg class="contacts__icon" viewBox="0 0 16 16" aria-hidden="true">
          <path d="M8 1 C4.7 1 3 3.4 3 6 C3 9.5 8 15 8 15 C8 15 13 9.5 13 6 C13 3.4 11.3 1 8 1 Z" fill="var(--brand-red)"/>
          <circle cx="8" cy="6" r="2" fill="#fff"/>
        </svg>
        PO Box 318, Warkworth, NZ,
      </li>
    </ul>

    <div class="wordmark">
      <span class="wordmark__ring" aria-hidden="true"></span>
      <p class="wordmark__text">Harwick Assurance<br>Partners Ltd</p>
    </div>
  </section>

  <section class="card card--back" aria-label="Business card back">
    <div class="wordmark">
      <span class="wordmark__ring" aria-hidden="true"></span>
      <p class="wordmark__text">Harwick Assurance<br>Partners Ltd</p>
    </div>
  </section>

</main>
</body>
</html>
```